Powerpoint to present for client our social media services along with a test case

we need a powerpoint template design that is modern looking and eye catching and keeps the client engaged. we are a social media agency based in Kuwait so the content will be bilingual in english and in Arabic. i will be providing the logo and you can design based upon the logo provided. the main tasks for this PPT is to show case our case studies and for sales presentation. the presentations will be a mix of visuals, texts, graphs and charts.
the ppt design has to reflect the company colors in the logo with the logo scattered to show it is done by the company.

It Company

```html
<!DOCTYPE html>
<html lang="en">
<head>
<meta charset="utf-8">
<title>Hollis Media — Presentation Template</title>
<link rel="stylesheet" href="https://fonts.googleapis.com/css2?family=Oswald:wght@400;500;600&family=Open+Sans:wght@400;600;700&display=swap">
<style>
:root{
  --stage:#000;
  --slide:#f5f5f5;
  --ink:#222;
  --copy:#8a8a8a;
  --muted:#b9b9b9;
  --red:#e3262a;
  --blue:#2b8fd3;
  --sky:#3fa6dd;
  --orange:#f39a1e;
  --green:#4b9a3b;
  --purple:#8a4c9f;
  --ring:#dedede;
  --white:#fff;
}
*{box-sizing:border-box;margin:0;padding:0}
html,body{width:1200px;height:1000px;overflow:hidden;background:var(--stage)}
.canvas{position:relative;width:1200px;height:1000px;background:var(--stage);font-family:'Open Sans',sans-serif}

.brand{position:absolute;left:72px;top:104px;display:flex;align-items:center;gap:10px;color:var(--white)}
.brand-square{width:22px;height:22px;background:var(--white)}
.brand-name{font:700 26px/1 'Open Sans',sans-serif}

.tagline{position:absolute;left:100px;top:892px;color:var(--white);font:500 29px/42px 'Oswald',sans-serif;text-transform:uppercase;letter-spacing:.3px}

.slide{position:absolute;width:280px;height:157px;background:var(--slide);overflow:hidden}
.slide::after{content:"";position:absolute;left:0;right:0;bottom:0;height:2px;
  background:linear-gradient(90deg,var(--red) 0 20%,var(--orange) 20% 40%,var(--green) 40% 60%,var(--blue) 60% 80%,var(--purple) 80% 100%)}
.mini-logo{position:absolute;left:8px;top:6px;display:flex;align-items:center;gap:3px;font:600 7px/1 'Open Sans',sans-serif;color:#9a9a9a}
.mini-logo::before{content:"";width:5px;height:5px;background:#9a9a9a}
.heading{position:absolute;left:0;top:38px;display:flex;align-items:center;gap:5px;font:500 9px/1 'Oswald',sans-serif;color:var(--ink);text-transform:uppercase}
.heading::before{content:"";width:14px;height:7px;background:var(--red);clip-path:polygon(0 0,72% 0,100% 50%,72% 100%,0 100%)}
.copy{position:absolute;font:400 3.6px/4.6px 'Open Sans',sans-serif;color:var(--copy)}
.sub{position:absolute;font:400 5.5px/1 'Open Sans',sans-serif;color:var(--blue)}
.label{position:absolute;font:500 4px/1 'Oswald',sans-serif;color:var(--white);text-transform:uppercase;display:flex;align-items:center;justify-content:center}
svg{position:absolute;left:0;top:0;overflow:visible}
.oswald{font-family:'Oswald',sans-serif}
.sans{font-family:'Open Sans',sans-serif}
</style>
</head>
<body>
<div class="canvas">

  <div class="brand"><span class="brand-square"></span><span class="brand-name">HOLLIS MEDIA</span></div>

  <!-- Row 1 -->
  <section class="slide" style="left:320px;top:53px">
    <div class="mini-logo" style="left:104px;top:72px;font-size:10px;gap:4px">HOLLIS MEDIA</div>
  </section>

  <section class="slide" style="left:605px;top:53px">
    <svg width="280" height="157">
      <g fill="none" stroke="var(--ring)" stroke-width="1">
        <circle cx="22" cy="26" r="13"/><circle cx="48" cy="12" r="6"/><circle cx="40" cy="52" r="9"/>
        <circle cx="190" cy="36" r="11"/><circle cx="258" cy="70" r="17"/><circle cx="232" cy="132" r="12"/><circle cx="70" cy="140" r="8"/>
      </g>
      <path d="M141 40a37 37 0 1 0 30 58l14 12-7-18a37 37 0 0 0-37-52z" fill="var(--white)" stroke="var(--blue)" stroke-width="1.4"/>
      <text x="141" y="80" text-anchor="middle" class="oswald" font-size="12" font-weight="600" fill="var(--ink)">WELCOME</text>
    </svg>
  </section>

  <section class="slide" style="left:890px;top:53px">
    <div class="mini-logo">HOLLIS</div>
    <svg width="280" height="157"><g fill="none" stroke="var(--ring)">
      <circle cx="252" cy="28" r="15"/><circle cx="220" cy="42" r="5"/><circle cx="262" cy="118" r="12"/><circle cx="238" cy="100" r="4"/>
    </g></svg>
    <div class="heading" style="left:40px;top:47px;color:var(--red)">Introduction</div>
    <div class="sub" style="left:40px;top:58px">Lorem ipsum dolor sit amet, dicam verea.</div>
    <p class="copy" style="left:40px;top:70px;width:165px">Lorem ipsum dolor sit amet, diam senet dorem sed in. Ne clio nonumy facilisis eu, id vis aliquip aliquid intereset. Si alio nibh idem, consectetur nunc elit duis.</p>
    <p class="copy" style="left:40px;top:86px;width:165px">Sit ut fugiat sumo nonummy, ea cu vim nulla mediocritatem. Eu quot virtute omittantur vix. In mea eirmod placerat audire.</p>
    <p class="copy" style="left:40px;top:100px;width:165px">Quo duo in tem. Nulla veri in harum est, vel at novum persequeris. Ei quo vero tempor, vix eu tollit debitis. Ius liber integre efficiantur ex, ludus veniam ne duo.</p>
  </section>

  <!-- Row 2 -->
  <section class="slide" style="left:35px;top:218px">
    <div class="mini-logo">HOLLIS</div>
    <div class="heading">About Us</div>
    <p class="copy" style="left:20px;top:50px;width:120px">Lorem ipsum dolor sit amet, diam senet dorem sed in. Ne clio nonumy facilisis eu, id vis aliquip aliquid intereset. Si alio nibh idem.</p>
    <div class="sub" style="left:20px;top:73px">Lorem ipsum</div>
    <p class="copy" style="left:20px;top:82px;width:120px">Lorem ipsum dolor sit amet, diam senet dorem sed in. Ne clio nonumy facilisis eu, id vis aliquip aliquid.</p>
    <div class="sub" style="left:20px;top:114px">Lorem ipsum</div>
    <p class="copy" style="left:20px;top:122px;width:120px">Lorem ipsum dolor sit amet, diam senet dorem sed in. Ne clio nonumy facilisis eu, id vis aliquip.</p>
    <svg width="280" height="157">
      <circle cx="181" cy="53" r="9" fill="var(--green)"/><rect x="177" y="50" width="8" height="5" rx="2" fill="var(--white)"/>
      <circle cx="181" cy="79" r="9" fill="var(--orange)"/><path d="M177 82l8-6" stroke="var(--white)" stroke-width="2"/>
      <circle cx="181" cy="105" r="9" fill="var(--red)"/><circle cx="181" cy="102" r="2.5" fill="var(--white)"/><path d="M176 110a5 4 0 0 1 10 0z" fill="var(--white)"/>
      <circle cx="181" cy="131" r="9" fill="var(--blue)"/><rect x="178" y="126" width="6" height="9" fill="var(--white)"/>
    </svg>
    <div class="sub" style="left:198px;top:44px;font-size:4.5px">Lorem ipsum</div><p class="copy" style="left:198px;top:50px;width:75px">Lorem ipsum dolor sit amet, diam senet dorem sed in nonumy.</p>
    <div class="sub" style="left:198px;top:70px;font-size:4.5px">Lorem ipsum</div><p class="copy" style="left:198px;top:76px;width:75px">Lorem ipsum dolor sit amet, diam senet dorem sed in nonumy.</p>
    <div class="sub" style="left:198px;top:96px;font-size:4.5px">Lorem ipsum</div><p class="copy" style="left:198px;top:102px;width:75px">Lorem ipsum dolor sit amet, diam senet dorem sed in nonumy.</p>
    <div class="sub" style="left:198px;top:122px;font-size:4.5px">Lorem ipsum</div><p class="copy" style="left:198px;top:128px;width:75px">Lorem ipsum dolor sit amet, diam senet dorem sed in nonumy.</p>
  </section>

  <section class="slide" style="left:320px;top:218px">
    <div class="mini-logo">HOLLIS</div>
    <div class="heading">Infographic Company</div>
    <div class="sub" style="left:24px;top:57px">01. Lorem ipsum</div>
    <p class="copy" style="left:24px;top:64px;width:100px">Lorem ipsum dolor sit amet, diam senet dorem sed in. Ne clio nonumy facilisis eu, id vis aliquip.</p>
    <div class="sub" style="left:24px;top:87px">02. Lorem ipsum</div>
    <p class="copy" style="left:24px;top:94px;width:100px">Lorem ipsum dolor sit amet, diam senet dorem sed in. Ne clio nonumy facilisis eu, id vis aliquip.</p>
    <div class="sub" style="left:24px;top:117px">03. Lorem ipsum</div>
    <p class="copy" style="left:24px;top:124px;width:100px">Lorem ipsum dolor sit amet, diam senet dorem sed in. Ne clio nonumy facilisis eu.</p>
    <svg width="280" height="157">
      <circle cx="161" cy="89" r="33" fill="var(--purple)" opacity=".9"/>
      <circle cx="207" cy="96" r="26" fill="var(--orange)" opacity=".9"/>
      <circle cx="249" cy="100" r="23" fill="var(--green)" opacity=".9"/>
      <g class="oswald" font-size="5" fill="var(--ink)"><text x="146" y="50">ORGANIZATION</text><text x="198" y="60">DISCIPLINE</text><text x="242" y="73">NICETY</text></g>
      <g class="oswald" font-size="6" fill="var(--white)"><text x="141" y="110">ONE</text><text x="193" y="110">TWO</text><text x="236" y="113">THREE</text></g>
    </svg>
  </section>

  <section class="slide" style="left:605px;top:218px">
    <div class="mini-logo">HOLLIS</div>
    <div class="heading">What We Offer</div>
    <div class="label" style="left:0;top:52px;width:56px;height:11px;background:var(--blue)">Creative Staff</div>
    <div class="label" style="left:56px;top:52px;width:56px;height:11px;background:var(--orange)">Flexible Work Hours</div>
    <div class="label" style="left:112px;top:52px;width:56px;height:11px;background:var(--red)">Flexible</div>
    <div class="label" style="left:168px;top:52px;width:56px;height:11px;background:var(--purple)">Innovative Minds</div>
    <div class="label" style="left:224px;top:52px;width:56px;height:11px;background:var(--green)">Stability</div>
    <svg width="280" height="157" fill="#333">
      <rect x="30" y="80" width="9" height="7"/><rect x="160" y="79" width="11" height="7" fill="none" stroke="#333" stroke-width="1.4"/><rect x="164" y="87" width="3" height="2"/>
      <path d="M30 124l9-9 1.5 1.5-9 9z"/><path d="M160 114l10 10M170 114l-10 10" stroke="#333" stroke-width="1.6"/>
    </svg>
    <div class="sub" style="left:48px;top:77px">Image description</div><p class="copy" style="left:48px;top:85px;width:100px">Lorem ipsum dolor sit amet, diam senet dorem sed in. Ne clio nonumy facilisis eu.</p>
    <div class="sub" style="left:180px;top:77px">Image description</div><p class="copy" style="left:180px;top:85px;width:90px">Lorem ipsum dolor sit amet, diam senet dorem sed in. Ne clio nonumy facilisis eu.</p>
    <div class="sub" style="left:48px;top:112px">Image description</div><p class="copy" style="left:48px;top:120px;width:100px">Lorem ipsum dolor sit amet, diam senet dorem sed in. Ne clio nonumy facilisis eu.</p>
    <div class="sub" style="left:180px;top:112px">Image description</div><p class="copy" style="left:180px;top:120px;width:90px">Lorem ipsum dolor sit amet, diam senet dorem sed in. Ne clio nonumy facilisis eu.</p>
  </section>

  <section class="slide" style="left:890px;top:218px">
    <svg width="280" height="157">
      <g stroke="#9bb7cc" stroke-width=".6">
        <line x1="140" y1="82" x2="37" y2="48"/><line x1="140" y1="82" x2="98" y2="37"/><line x1="140" y1="82" x2="198" y2="40"/>
        <line x1="140" y1="82" x2="250" y2="20"/><line x1="140" y1="82" x2="258" y2="73"/><line x1="140" y1="82" x2="217" y2="93"/>
        <line x1="140" y1="82" x2="242" y2="131"/><line x1="140" y1="82" x2="95" y2="134"/><line x1="140" y1="82" x2="35" y2="125"/>
        <line x1="140" y1="82" x2="65" y2="82"/>
      </g>
      <path d="M140 50a32 32 0 1 0 26 52l12 9-6-15a32 32 0 0 0-32-46z" fill="var(--white)" stroke="var(--blue)" stroke-width="1.3"/>
      <text x="140" y="80" text-anchor="middle" class="oswald" font-size="8" font-weight="500" fill="var(--ink)">ONLINE</text>
      <text x="140" y="91" text-anchor="middle" class="oswald" font-size="8" font-weight="500" fill="var(--ink)">MARKETING</text>
      <circle cx="37" cy="48" r="9" fill="var(--blue)"/><circle cx="98" cy="37" r="9" fill="var(--sky)"/>
      <circle cx="198" cy="40" r="9" fill="var(--sky)"/><circle cx="250" cy="20" r="9" fill="var(--red)"/>
      <circle cx="258" cy="73" r="9" fill="var(--blue)"/><circle cx="217" cy="93" r="9" fill="var(--blue)"/>
      <circle cx="242" cy="131" r="9" fill="var(--red)"/><circle cx="95" cy="134" r="9" fill="var(--orange)"/>
      <circle cx="35" cy="125" r="9" fill="var(--orange)"/><circle cx="65" cy="82" r="9" fill="var(--green)"/>
      <rect x="60" y="78.5" width="10" height="7" fill="var(--white)"/><path d="M60 78.5l5 4 5-4" fill="none" stroke="var(--green)" stroke-width=".8"/>
      <path d="M31 120c0 6 6 11 11 11l1-3-3-2-2 1c-2-1-3-2-4-4l1-2-2-3z" fill="var(--white)"/>
    </svg>
  </section>

  <!-- Row 3 -->
  <section class="slide" style="left:35px;top:383px">
    <div class="mini-logo">HOLLIS</div>
    <div class="heading">SWOT Analysis</div>
    <div class="label" style="left:30px;top:53px;width:70px;height:11px;background:var(--blue)">Strengths</div>
    <div class="label" style="left:157px;top:53px;width:70px;height:11px;background:var(--green)">Weaknesses</div>
    <div class="label" style="left:30px;top:109px;width:70px;height:11px;background:var(--red)">Opportunities</div>
    <div class="label" style="left:157px;top:109px;width:70px;height:11px;background:var(--purple)">Threats</div>
    <p class="copy" style="left:44px;top:72px;width:80px">1. Original + Creative Designs<br>2. High quality materials<br>3. User friendly website<br>4. Online sales presence<br>5. Low start-up cost</p>
    <p class="copy" style="left:170px;top:72px;width:80px">1. Ease of entry into the market<br>2. New company in a market of established players</p>
    <p class="copy" style="left:44px;top:128px;width:80px">1. The ability to expand into new markets via online sales<br>2. Able to extend the product line to include new offers</p>
    <p class="copy" style="left:170px;top:128px;width:80px">1. Ease of entry into the market<br>2. Meeting high demand in a short period of time</p>
  </section>

  <section class="slide" style="left:320px;top:383px">
    <div class="mini-logo">HOLLIS</div>
    <div class="heading">Our Team</div>
    <div class="label" style="left:16px;top:102px;width:55px;height:7px;background:var(--red);font-size:3.4px">Managing Director</div>
    <div class="label" style="left:79px;top:102px;width:55px;height:7px;background:var(--red);font-size:3.4px">Creative Director</div>
    <div class="label" style="left:143px;top:102px;width:55px;height:7px;background:var(--red);font-size:3.4px">Finance Manager</div>
    <div class="label" style="left:207px;top:102px;width:55px;height:7px;background:var(--red);font-size:3.4px">Head of Human Resources</div>
    <div class="oswald" style="position:absolute;left:16px;top:116px;font-size:5px;color:var(--ink)">DANA ROSS</div>
    <div class="oswald" style="position:absolute;left:79px;top:116px;font-size:5px;color:var(--ink)">DANA ROSS</div>
    <div class="oswald" style="position:absolute;left:143px;top:116px;font-size:5px;color:var(--ink)">DANA ROSS</div>
    <div class="oswald" style="position:absolute;left:207px;top:116px;font-size:5px;color:var(--ink)">DANA ROSS</div>
    <p class="copy" style="left:16px;top:124px;width:55px">Lorem ipsum dolor sit amet, consectetur adipiscing elit, aenean enim a felis.</p>
    <p class="copy" style="left:79px;top:124px;width:55px">Lorem ipsum dolor sit amet, consectetur adipiscing elit, aenean enim a felis.</p>
    <p class="copy" style="left:143px;top:124px;width:55px">Lorem ipsum dolor sit amet, consectetur adipiscing elit, aenean enim a felis.</p>
    <p class="copy" style="left:207px;top:124px;width:55px">Lorem ipsum dolor sit amet, consectetur adipiscing elit, aenean enim a felis.</p>
  </section>

  <section class="slide" style="left:605px;top:383px">
    <div class="mini-logo">HOLLIS</div>
    <div class="heading">Infographic Element</div>
    <svg width="280" height="157">
      <g fill="none" stroke-width="4">
        <circle cx="42" cy="80" r="16" stroke="#3a3a3a"/><circle cx="42" cy="80" r="16" stroke="var(--red)" stroke-dasharray="50.3 100.5" transform="rotate(-90 42 80)"/>
        <circle cx="106" cy="80" r="16" stroke="#3a3a3a"/><circle cx="106" cy="80" r="16" stroke="var(--red)" stroke-dasharray="74.4 100.5" transform="rotate(-90 106 80)"/>
        <circle cx="170" cy="80" r="16" stroke="#3a3a3a"/><circle cx="170" cy="80" r="16" stroke="var(--red)" stroke-dasharray="82.4 100.5" transform="rotate(-90 170 80)"/>
        <circle cx="234" cy="80" r="16" stroke="#3a3a3a"/><circle cx="234" cy="80" r="16" stroke="var(--red)" stroke-dasharray="95.5 100.5" transform="rotate(-90 234 80)"/>
      </g>
      <g class="oswald" font-size="9" text-anchor="middle" fill="var(--ink)">
        <text x="42" y="83">50%</text><text x="106" y="83">74%</text><text x="170" y="83">82%</text><text x="234" y="83">95%</text>
      </g>
    </svg>
    <div class="label" style="left:20px;top:110px;width:44px;height:7px;background:var(--blue)">Lorem: 400,000</div>
    <div class="label" style="left:84px;top:110px;width:44px;height:7px;background:var(--blue)">Lorem: 400,000</div>
    <div class="label" style="left:148px;top:110px;width:44px;height:7px;background:var(--blue)">Lorem: 400,000</div>
    <div class="label" style="left:212px;top:110px;width:44px;height:7px;background:var(--blue)">Lorem: 400,000</div>
    <p class="copy" style="left:20px;top:130px;width:240px">Lorem ipsum dolor sit amet, diam senet dorem sed in. Ne clio nonumy facilisis eu, id vis aliquip aliquid intereset. Si alio nibh idem, consectetur nunc elit duis vis ex. Lorem ipsum dolor sit amet, diam senet dorem sed in tempor.</p>
  </section>

  <section class="slide" style="left:890px;top:383px">
    <div class="mini-logo">HOLLIS</div>
    <div class="heading">Graphic</div>
    <div class="sub" style="left:18px;top:54px">About This Graphic Chart</div>
    <p class="copy" style="left:18px;top:62px;width:120px">Lorem ipsum dolor sit amet, diam senet dorem sed in. Ne clio nonumy facilisis eu.</p>
    <div class="oswald" style="position:absolute;left:18px;top:79px;font-size:5px;color:var(--ink)">2010</div><p class="copy" style="left:18px;top:86px;width:55px">Some text about SKILLS related goes here. Some text about SKILLS related.</p>
    <div class="oswald" style="position:absolute;left:82px;top:79px;font-size:5px;color:var(--ink)">2011</div><p class="copy" style="left:82px;top:86px;width:55px">Some text about SKILLS related goes here. Some text about SKILLS related.</p>
    <div class="oswald" style="position:absolute;left:18px;top:109px;font-size:5px;color:var(--ink)">2012</div><p class="copy" style="left:18px;top:116px;width:55px">Some text about SKILLS related goes here. Some text about SKILLS related.</p>
    <div class="oswald" style="position:absolute;left:82px;top:109px;font-size:5px;color:var(--ink)">2013</div><p class="copy" style="left:82px;top:116px;width:55px">Some text about SKILLS related goes here. Some text about SKILLS related.</p>
    <svg width="280" height="157">
      <g stroke="#e4e4e4" stroke-width=".5"><line x1="148" y1="45" x2="265" y2="45"/><line x1="148" y1="62" x2="265" y2="62"/><line x1="148" y1="79" x2="265" y2="79"/><line x1="148" y1="96" x2="265" y2="96"/><line x1="148" y1="113" x2="265" y2="113"/></g>
      <rect x="152" y="100" width="7" height="24" fill="var(--red)"/><rect x="159" y="47" width="7" height="77" fill="var(--orange)"/><rect x="166" y="72" width="7" height="52" fill="var(--green)"/>
      <rect x="180" y="108" width="7" height="16" fill="var(--red)"/><rect x="187" y="73" width="7" height="51" fill="var(--orange)"/><rect x="194" y="78" width="7" height="46" fill="var(--green)"/>
      <rect x="208" y="94" width="7" height="30" fill="var(--red)"/><rect x="215" y="42" width="7" height="82" fill="var(--orange)"/><rect x="222" y="66" width="7" height="58" fill="var(--green)"/>
      <rect x="236" y="104" width="7" height="20" fill="var(--red)"/><rect x="243" y="98" width="7" height="26" fill="var(--orange)"/><rect x="250" y="102" width="7" height="22" fill="var(--green)"/>
      <g class="oswald" font-size="4" fill="#666" text-anchor="middle"><text x="162" y="130">2010</text><text x="190" y="130">2011</text><text x="218" y="130">2012</text><text x="246" y="130">2013</text></g>
      <rect x="152" y="136" width="8" height="3" fill="var(--red)"/><rect x="188" y="136" width="8" height="3" fill="var(--orange)"/><rect x="224" y="136" width="8" height="3" fill="var(--green)"/>
      <g class="sans" font-size="3" fill="#777"><text x="162" y="139">Description</text><text x="198" y="139">Description</text><text x="234" y="139">Description</text></g>
    </svg>
  </section>

  <!-- Row 4 -->
  <section class="slide" style="left:35px;top:548px">
    <div class="mini-logo">HOLLIS</div>
    <div class="heading">Monthly Sales</div>
    <p class="copy" style="left:18px;top:50px;width:120px">Lorem ipsum dolor sit amet, diam senet dorem sed in. Ne clio nonumy facilisis eu, id vis aliquip aliquid.</p>
    <div class="label" style="left:30px;top:70px;width:14px;height:8px;background:var(--blue)">58%</div><p class="copy" style="left:50px;top:70px;width:85px">Lorem ipsum dolor sit amet, diam senet dorem sed in nonumy.</p>
    <div class="label" style="left:30px;top:90px;width:14px;height:8px;background:var(--red)">23%</div><p class="copy" style="left:50px;top:90px;width:85px">Lorem ipsum dolor sit amet, diam senet dorem sed in nonumy.</p>
    <div class="label" style="left:30px;top:110px;width:14px;height:8px;background:var(--orange)">10%</div><p class="copy" style="left:50px;top:110px;width:85px">Lorem ipsum dolor sit amet, diam senet dorem sed in nonumy.</p>
    <div class="label" style="left:30px;top:130px;width:14px;height:8px;background:var(--green)">9%</div><p class="copy" style="left:50px;top:130px;width:85px">Lorem ipsum dolor sit amet, diam senet dorem sed in nonumy.</p>
    <svg width="280" height="157">
      <g fill="none" stroke-width="37" transform="rotate(-90 207 96)">
        <circle cx="207" cy="96" r="18.5" stroke="var(--blue)" stroke-dasharray="67.4 116.3"/>
        <circle cx="207" cy="96" r="18.5" stroke="var(--red)" stroke-dasharray="26.7 116.3" stroke-dashoffset="-67.4"/>
        <circle cx="207" cy="96" r="18.5" stroke="var(--orange)" stroke-dasharray="11.6 116.3" stroke-dashoffset="-94.1"/>
        <circle cx="207" cy="96" r="18.5" stroke="var(--green)" stroke-dasharray="10.6 116.3" stroke-dashoffset="-105.7"/>
      </g>
      <g class="sans" font-size="4" fill="var(--white)"><text x="222" y="98">58%</text><text x="183" y="103">23%</text><text x="183" y="75">10%</text><text x="197" y="64">9%</text></g>
      <g class="sans" font-size="3" fill="#555">
        <circle cx="165" cy="138" r="1.5" fill="var(--blue)"/><text x="168" y="139">1ST QTR</text>
        <circle cx="190" cy="138" r="1.5" fill="var(--red)"/><text x="193" y="139">2ND QTR</text>
        <circle cx="215" cy="138" r="1.5" fill="var(--orange)"/><text x="218" y="139">3RD QTR</text>
        <circle cx="240" cy="138" r="1.5" fill="var(--green)"/><text x="243" y="139">4TH QTR</text>
      </g>
    </svg>
  </section>

  <section class="slide" style="left:320px;top:548px">
    <div class="mini-logo">HOLLIS</div>
    <div class="heading">Pyramid Smart Art</div>
    <p class="copy" style="left:18px;top:50px;width:240px">Lorem ipsum dolor sit amet, diam senet dorem sed in. Ne clio nonumy facilisis eu, id vis aliquip aliquid intereset.</p>
    <svg width="280" height="157">
      <polygon points="142,70 131.7,84 152.3,84" fill="var(--sky)"/>
      <polygon points="130.3,86 153.7,86 164,100 120,100" fill="var(--blue)"/>
      <polygon points="118.5,102 165.5,102 175,115 109,115" fill="var(--red)"/>
      <polygon points="107.6,117 176.4,117 186,130 98,130" fill="var(--blue)"/>
      <polygon points="96.5,132 187.5,132 197,145 87,145" fill="var(--blue)"/>
      <g class="sans" fill="var(--white)" text-anchor="middle">
        <text x="142" y="82" font-size="3.5">Price</text>
        <text x="142" y="95" font-size="4.5">Promotion</text>
        <text x="142" y="110.5" font-size="4.5">People</text>
        <text x="142" y="125.5" font-size="4.5">Place</text>
        <text x="142" y="140.5" font-size="4.5">Distribution</text>
      </g>
    </svg>
  </section>

  <section class="slide" style="left:605px;top:548px">
    <div class="mini-logo">HOLLIS</div>
    <div class="heading">Performance</div>
    <svg width="280" height="157">
      <g fill="none" stroke="var(--red)" stroke-width=".6">
        <rect x="106" y="60" width="14" height="7"/><rect x="68" y="73" width="14" height="7"/><rect x="60" y="86" width="14" height="7"/>
        <rect x="106" y="99" width="14" height="7"/><rect x="133" y="112" width="14" height="7"/><rect x="97" y="125" width="14" height="7"/>
      </g>
      <rect x="28" y="60" width="76" height="7" fill="var(--green)"/><rect x="28" y="73" width="38" height="7" fill="var(--red)"/>
      <rect x="28" y="86" width="30" height="7" fill="var(--green)"/><rect x="28" y="99" width="76" height="7" fill="var(--green)"/>
      <rect x="28" y="112" width="103" height="7" fill="var(--green)"/><rect x="28" y="125" width="67" height="7" fill="var(--green)"/>
      <g class="oswald" font-size="4" fill="var(--white)"><text x="31" y="65.5">LOREM</text><text x="31" y="78.5">LOREM</text><text x="31" y="91.5">LOREM</text><text x="31" y="104.5">LOREM</text><text x="31" y="117.5">LOREM</text><text x="31" y="130.5">LOREM</text></g>
      <g class="oswald" font-size="4" fill="var(--red)" text-anchor="middle"><text x="113" y="65.5">80%</text><text x="75" y="78.5">90%</text><text x="67" y="91.5">93%</text><text x="113" y="104.5">80%</text><text x="140" y="117.5">83%</text><text x="104" y="130.5">50%</text></g>
    </svg>
    <p class="copy" style="left:165px;top:60px;width:90px">Lorem ipsum dolor sit amet, diam senet dorem sed in. Ne clio nonumy facilisis eu, id vis aliquip aliquid.</p>
    <p class="copy" style="left:165px;top:84px;width:90px">Lorem ipsum dolor sit amet, diam senet dorem sed in. Ne clio nonumy facilisis eu, id vis aliquip aliquid.</p>
    <p class="copy" style="left:165px;top:108px;width:90px">Lorem ipsum dolor sit amet, diam senet dorem sed in. Ne clio nonumy facilisis eu, id vis aliquip aliquid.</p>
  </section>

  <section class="slide" style="left:890px;top:548px">
    <div class="mini-logo">HOLLIS</div>
    <div class="heading">Two Column Layout</div>
    <div class="label" style="left:28px;top:55px;width:96px;height:8px;background:var(--red);justify-content:flex-start;padding-left:4px">Insert heading here</div>
    <div class="label" style="left:154px;top:55px;width:96px;height:8px;background:var(--red);justify-content:flex-start;padding-left:4px">Insert heading here</div>
    <p class="copy" style="left:28px;top:70px;width:98px">Lorem ipsum dolor sit amet, diam senet dorem sed in. Ne clio nonumy facilisis eu, id vis aliquip aliquid intereset. Si alio nibh idem, consectetur nunc elit duis vis ex mediocritatem.<br><br>Quo duo in tem. Nulla veri in harum est, vel at novum persequeris. Ei quo vero tempor, vix eu tollit debitis. Ius liber integre efficiantur ex, ludus veniam ne duo, his cu dicta.</p>
    <p class="copy" style="left:154px;top:70px;width:98px">Lorem ipsum dolor sit amet, diam senet dorem sed in. Ne clio nonumy facilisis eu, id vis aliquip aliquid intereset. Si alio nibh idem, consectetur nunc elit duis vis ex mediocritatem.<br><br>Quo duo in tem. Nulla veri in harum est, vel at novum persequeris. Ei quo vero tempor, vix eu tollit debitis. Ius liber integre efficiantur ex, ludus veniam ne duo.</p>
  </section>

  <!-- Row 5 -->
  <section class="slide" style="left:35px;top:713px">
    <div class="mini-logo">HOLLIS</div>
    <div class="heading">Plan Components</div>
    <svg width="280" height="157">
      <circle cx="67" cy="82" r="24" fill="var(--green)" opacity=".9"/>
      <circle cx="112" cy="82" r="24" fill="var(--orange)" opacity=".9"/>
      <circle cx="157" cy="82" r="24" fill="var(--sky)" opacity=".9"/>
      <circle cx="202" cy="82" r="24" fill="var(--purple)" opacity=".9"/>
      <g class="oswald" font-size="4" fill="var(--white)" text-anchor="middle"><text x="67" y="84">IMAGE</text><text x="112" y="84">IMAGE</text><text x="157" y="84">IMAGE</text><text x="202" y="84">IMAGE</text></g>
    </svg>
    <p class="copy" style="left:28px;top:118px;width:230px">Lorem ipsum dolor sit amet, diam senet dorem sed in. Ne clio nonumy facilisis eu, id vis aliquip aliquid intereset. Si alio nibh idem, consectetur nunc elit.</p>
    <p class="copy" style="left:28px;top:132px;width:230px">Quo duo in tem. Nulla veri in harum est, vel at novum persequeris. Ei quo vero tempor, vix eu tollit debitis. Ius liber integre efficiantur ex, ludus veniam ne duo, his cu dicta dolore.</p>
  </section>

  <section class="slide" style="left:320px;top:713px">
    <div class="mini-logo">HOLLIS</div>
    <div class="heading">Partnership</div>
    <p class="copy" style="left:18px;top:50px;width:240px">Lorem ipsum dolor sit amet, diam senet dorem sed in. Ne clio nonumy facilisis eu, id vis aliquip aliquid intereset. Si alio nibh idem, consectetur nunc elit duis vis ex mediocritatem.</p>
    <svg width="280" height="157">
      <polygon points="35,84 44,72 60,72 69,84 60,96 44,96" fill="var(--blue)"/>
      <polygon points="36,100 68,100 61,112 43,112" fill="var(--orange)"/>
      <polygon points="152,74 159,64 179,64 186,74" fill="var(--blue)"/>
      <polygon points="152,78 186,78 186,92 179,104 159,104 152,92" fill="var(--orange)"/>
      <g class="oswald" font-size="7" fill="var(--white)" text-anchor="middle"><text x="52" y="87">85%</text><text x="52" y="109">15%</text><text x="169" y="72">30%</text><text x="169" y="94">70%</text></g>
    </svg>
    <div class="sub" style="left:84px;top:76px">Image description</div><p class="copy" style="left:84px;top:84px;width:60px">Lorem ipsum dolor sit amet, diam senet dorem sed in. Ne clio nonumy.</p>
    <div class="sub" style="left:200px;top:76px">Image description</div><p class="copy" style="left:200px;top:84px;width:60px">Lorem ipsum dolor sit amet, diam senet dorem sed in. Ne clio nonumy.</p>
  </section>

  <section class="slide" style="left:605px;top:713px">
    <svg width="280" height="157">
      <g fill="none" stroke="var(--ring)">
        <circle cx="20" cy="24" r="13"/><circle cx="46" cy="10" r="6"/><circle cx="38" cy="52" r="9"/><circle cx="206" cy="36" r="11"/>
        <circle cx="256" cy="68" r="17"/><circle cx="232" cy="132" r="12"/><circle cx="72" cy="138" r="8"/><circle cx="150" cy="120" r="5"/>
      </g>
      <text x="140" y="79" text-anchor="middle" class="oswald" font-size="9" font-weight="500" fill="var(--ink)">ASK ME YOUR QUESTIONS !</text>
    </svg>
  </section>

  <section class="slide" style="left:890px;top:713px">
    <div class="mini-logo">HOLLIS</div>
    <svg width="280" height="157">
      <g fill="none" stroke="var(--ring)"><circle cx="252" cy="28" r="15"/><circle cx="220" cy="42" r="5"/><circle cx="262" cy="118" r="12"/><circle cx="40" cy="120" r="8"/></g>
      <path d="M144 38a38 38 0 1 0 30 60l16 15-8-20a38 38 0 0 0-38-55z" fill="var(--white)" stroke="var(--blue)" stroke-width="1.4"/>
      <text x="144" y="78" text-anchor="middle" class="oswald" font-size="13" font-weight="500" fill="var(--ink)">THANK YOU</text>
      <text x="144" y="89" text-anchor="middle" class="sans" font-size="5.5" fill="#555">Your Name</text>
    </svg>
  </section>

  <p class="tagline">Fully editable with motion effects. Contains: original presentation document,<br>file with vector icons</p>

</div>
</body>
</html>
```